NOTE: I PROVIDED THE INCORRECT LOGO AND ONLY A HANDFUL OF PEOPLE NOTICED THAT IT WAS NOT THE ONE I DESCRIBED. THE LOGO I HAVE NOW ATTACHED MATCHES MY WEBSITE AND THE COLORS ON THE WEBSITE SHOULD BE USED FOR THE CARD.

PLEASE READ THE BUSINESS CARD DETAILS AND PROJECT MUST HAVES CAREFULLY.

I am looking for a business card that is powerful, a bit edgy, and although I work in the corporate world, not too formal. I would like to see designs that use the colors on my website www.brightmoorlane.com. I don't want the card to look washed out so please use shades of those colors that make them "pop". The "vibe" of the card needs to show substance and confidence while also reflecting that we're not your usual consultants.

The focus of my work is turning "people problems" into profits. Those problems could be poor service, an unstable workforce, untrained leaders, or managing change. We are an aggressive, results-focused team of performance improvement professionals who refuse to believe "things can't be done". For us, failure is not an option. Our logo reflects a target from the view of the site on a gun.

In addition to the contact information provided on the sample business card (do not include "turning people problems into profits"), I would like to include this statement (probably on the back):
I equip results-oriented business leaders to turn their people problems into profits in six months or less.

PLEASE NOTE THAT MY WEBSITE IS UNDER REVISION TO TONE DOWN THE MILITARY THEME, ALTHOUGH THE WARRIOR ENERGY AND FOCUS ON RESULTS REMAINS.

Target Market(s)

My clients are Mid and senior-level managers. I don't target any particular industry.

Industry/Entity Type

Consulting

Contact Information for Business Card

In addition to the contact information provided on the sample business card (DO NOT INCLUDE "turning people problems into profits"), I would like to include this statement (probably on the back):

I don't care whether the card is landscape or portrait view.

Font styles to use
Sans Serif

Requirements
Must have
• 1. be easy to read, no 6-8 point fonts!
• 2. a "vibe" that captures the eye without being too chaotic or busy
• 3. bold color, not washed out or boring - a good blend with the colors currently on my website (black, red, white, army green) but you don't need to use all of them.
• 4. all the contact information I have provided
• 5. a good blend with the colors currently on my website
• 6. Must have this quote on the back of the card: I equip results-oriented business leaders to turn their people problems into profits in six months or less.
Nice to have
• In looking at the sample images I provided for ideas, you can see that I like the way a card carries over from one side to the next.
• It would be great to find some aspect/quality/feature that I haven't seen before
Should not have
• 1. NO use of ALL CAPS
• 2. fonts that I would have to seek out and purchase (you should provide files for font if using something not standard)

```html
<!DOCTYPE html>
<html lang="en">
<head>
<meta charset="utf-8">
<title>Brightmoor Lane – Business Card</title>
<link href="https://fonts.googleapis.com/css2?family=Roboto+Condensed:wght@400;700&display=swap" rel="stylesheet">
<style>
  :root {
    --stage: #e9e6e1;
    --card: #232022;
    --card-back: #1e1c1d;
    --pattern: #2b2829;
    --white: #ffffff;
    --muted: #d9d6d4;
    --red: #e0262b;
    --rule: #bdb9b7;
  }
  * { margin: 0; padding: 0; box-sizing: border-box; }
  html, body { width: 1200px; height: 886px; overflow: hidden; }
  body {
    background: var(--stage);
    font-family: "Roboto Condensed", Arial, sans-serif;
    position: relative;
  }
  .card {
    position: absolute;
    left: 320px;
    width: 560px;
    height: 320px;
    border-radius: 4px;
    box-shadow: 0 8px 24px rgba(0,0,0,.25);
    overflow: hidden;
  }
  .card--front { top: 103px; background: var(--card); }
  .card--back { top: 463px; background: var(--card-back); }

  /* brand name lockup */
  .brand {
    position: absolute;
    display: flex;
    align-items: center;
    gap: 14px;
    color: var(--white);
    font-weight: 700;
    line-height: 1;
  }
  .brand__dot {
    border-radius: 50%;
    background: var(--white);
    flex: none;
  }
  .brand__name { display: flex; flex-direction: column; }
  .card--front .brand { right: 44px; top: 34px; font-size: 32px; }
  .card--front .brand__dot { width: 56px; height: 56px; }
  .card--back .brand { left: 50%; top: 70px; transform: translateX(-50%); font-size: 44px; }
  .card--back .brand__dot { width: 84px; height: 84px; }

  /* contact column */
  .contact-rule {
    position: absolute;
    left: 62px; top: 0; bottom: 0;
    width: 1px;
    background: var(--rule);
  }
  .contact-list {
    position: absolute;
    left: 46px; top: 122px;
    list-style: none;
  }
  .contact-list li {
    display: flex;
    align-items: center;
    height: 36px;
    color: var(--muted);
    font-size: 15px;
  }
  .contact-list li.is-person { height: 50px; }
  .contact-icon {
    width: 33px; height: 33px;
    border-radius: 50%;
    background: var(--white);
    display: flex; align-items: center; justify-content: center;
    margin-right: 22px;
    flex: none;
  }
  .contact-icon svg { width: 17px; height: 17px; fill: var(--card); }
  .person { line-height: 1.15; }
  .person__name { display: block; color: var(--white); font-size: 20px; font-weight: 700; }
  .person__title { display: block; color: var(--red); font-size: 15px; }

  /* back */
  .back-pattern {
    position: absolute; inset: 0;
    background: radial-gradient(circle at 50% 50%, var(--pattern), var(--card-back));
  }
  .statement {
    position: absolute;
    left: 70px; right: 70px; top: 206px;
    text-align: center;
    color: var(--muted);
    font-size: 16px;
    line-height: 1.4;
  }
</style>
</head>
<body>

<section class="card card--front" aria-label="Business card front">
  <div class="brand">
    <span class="brand__dot"></span>
    <span class="brand__name"><span>Brightmoor</span><span>Lane</span></span>
  </div>

  <div class="contact-rule"></div>
  <ul class="contact-list">
    <li class="is-person">
      <span class="contact-icon"><svg viewBox="0 0 20 20"><circle cx="10" cy="6" r="4"/><path d="M2 19c0-5 3.5-7 8-7s8 2 8 7z"/></svg></span>
      <span class="person">
        <span class="person__name">Dana Whitfield</span>
        <span class="person__title">Chief Performance Strategist</span>
      </span>
    </li>
    <li>
      <span class="contact-icon"><svg viewBox="0 0 20 20"><path d="M5 2l3 4-2 2c1 2 3 4 5 5l2-2 4 3-2 3C9 17 3 11 2 5z"/></svg></span>
      555-210-4418
    </li>
    <li>
      <span class="contact-icon"><svg viewBox="0 0 20 20"><path d="M5 1h10v18H5zM7 3v12h6V3z"/></svg></span>
      555-307-2291
    </li>
    <li>
      <span class="contact-icon"><svg viewBox="0 0 20 20"><path d="M2 4h16v12H2zM3.5 5.5l6.5 5 6.5-5z" fill-rule="evenodd"/></svg></span>
      danaw@brightmoorlane.com
    </li>
    <li>
      <span class="contact-icon"><svg viewBox="0 0 20 20"><path d="M10 1a9 9 0 1 0 0 18 9 9 0 0 0 0-18zm0 2c1.5 1.5 2.3 4 2.3 7s-.8 5.5-2.3 7c-1.5-1.5-2.3-4-2.3-7S8.5 4.5 10 3z" fill-rule="evenodd"/></svg></span>
      www.brightmoorlane.com
    </li>
  </ul>
</section>

<section class="card card--back" aria-label="Business card back">
  <div class="back-pattern" role="img" aria-label="Repeating faint brand-mark pattern across the card"></div>
  <div class="brand">
    <span class="brand__dot"></span>
    <span class="brand__name"><span>Brightmoor</span><span>Lane</span></span>
  </div>
  <p class="statement">I equip results-oriented business leaders to turn their people problems into profits in six months or less.</p>
</section>

</body>
</html>
```